Krelvo, a service provider dedicated to improving the performance of a website

Krelvo offers optimization and performance improvement for all types of websites (showcase sites, e-commerce, ...), with the aim of improving their ranking on Searvo and their customer transformation rate. The main benefits consist in optimizing the factors of a site. In addition, we also offer content creation (description of product sheets, services, ...), Searvo Ads campaign management, migration version for Prestashop / Wordpress, etc. The design must be a fresh image, dynamic, why not "fun", but also serious. No favorite color, carte blanche on this point;)

```html
<!DOCTYPE html>
<html lang="en">
<head>
<meta charset="utf-8">
<title>Krelvo business card</title>
<link href="https://fonts.googleapis.com/css2?family=Roboto:wght@400;700&display=swap" rel="stylesheet">
<style>
  :root {
    --brand-blue: #3b55a9;
    --brand-blue-line: #2f47a0;
    --paper: #fbfbfa;
    --ink-grey: #55585e;
    --backdrop: #d9d9d7;
  }
  * { margin: 0; padding: 0; box-sizing: border-box; }
  html, body { width: 1200px; height: 839px; overflow: hidden; }
  body {
    background: var(--backdrop);
    font-family: "Roboto", Arial, sans-serif;
    position: relative;
  }
  .card {
    position: absolute;
    top: 270px;
    width: 520px;
    height: 298px;
    box-shadow: 0 10px 24px rgba(0,0,0,0.18);
  }
  .card--front { left: 50px; background: var(--paper); }
  .card--back  { left: 630px; background: var(--brand-blue); }

  .wordmark {
    position: absolute;
    font-weight: 700;
    letter-spacing: -1px;
    line-height: 1;
  }
  .card--front .wordmark {
    right: 70px; top: 34px;
    font-size: 60px;
    color: var(--brand-blue);
  }
  .card--back .wordmark {
    right: 60px; top: 150px;
    font-size: 74px;
    color: #ffffff;
  }

  .identity {
    position: absolute;
    left: 56px; top: 110px;
  }
  .identity__name {
    color: var(--brand-blue);
    font-weight: 700;
    font-size: 15px;
    letter-spacing: 0.3px;
  }
  .identity__role {
    color: var(--ink-grey);
    font-size: 15px;
    margin-top: 1px;
  }
  .divider {
    position: absolute;
    left: 56px; right: 40px; top: 156px;
    height: 1px;
    background: var(--brand-blue-line);
  }
  .contacts {
    position: absolute;
    left: 56px; top: 168px;
    list-style: none;
  }
  .contacts li {
    display: flex;
    align-items: center;
    gap: 8px;
    color: var(--ink-grey);
    font-size: 15px;
    height: 22px;
  }
  .contacts svg { width: 15px; height: 15px; flex: none; }
  .address {
    position: absolute;
    right: 40px; top: 172px;
    text-align: right;
    color: var(--ink-grey);
    font-size: 15px;
    line-height: 1.35;
  }
</style>
</head>
<body>
  <section class="card card--front" aria-label="Business card front">
    <div class="wordmark">Krelvo</div>
    <div class="identity">
      <div class="identity__name">MARCUS LINDQVIST</div>
      <div class="identity__role">Founder &amp; CEO</div>
    </div>
    <div class="divider"></div>
    <ul class="contacts">
      <li>
        <svg viewBox="0 0 16 16"><circle cx="8" cy="8" r="8" fill="var(--brand-blue)"/><path d="M5.3 4.2l1.4 1.6-.8 1c.5 1.1 1.3 1.9 2.4 2.4l1-.8 1.6 1.4-.8 1.3c-2.8-.3-5.1-2.6-5.4-5.4z" fill="#fff"/></svg>
        (555) 214-7730
      </li>
      <li>
        <svg viewBox="0 0 16 16"><circle cx="8" cy="8" r="8" fill="var(--brand-blue)"/><rect x="5.5" y="4" width="5" height="2.5" fill="#fff"/><rect x="4" y="7" width="8" height="3.5" rx="0.6" fill="#fff"/><rect x="5.5" y="10" width="5" height="2" fill="#fff"/></svg>
        (555) 381-0462
      </li>
      <li>
        <svg viewBox="0 0 16 16"><circle cx="8" cy="8" r="8" fill="var(--brand-blue)"/><rect x="4" y="5.2" width="8" height="5.6" fill="#fff"/><path d="M4 5.2l4 3 4-3" fill="none" stroke="var(--brand-blue)" stroke-width="0.9"/></svg>
        hello@krelvoweb.com
      </li>
      <li>
        <svg viewBox="0 0 16 16"><circle cx="8" cy="8" r="8" fill="var(--brand-blue)"/><g fill="none" stroke="#fff" stroke-width="0.9"><circle cx="8" cy="8" r="4.2"/><ellipse cx="8" cy="8" rx="1.8" ry="4.2"/><path d="M3.8 8h8.4M4.5 6h7M4.5 10h7"/></g></svg>
        www.krelvoweb.com
      </li>
    </ul>
    <div class="address">
      Harbor Rd 48, Suite 12<br>
      Zip 20451, Norway
    </div>
  </section>

  <section class="card card--back" aria-label="Business card back">
    <div class="wordmark">Krelvo</div>
  </section>
</body>
</html>
```